Business card design for IT consulting company

Looking for a simple, modern, clean business card design.
Open to reworking our existing logo.

Attached is our current business cards which we do not like.
Ideally double sided with something simple on the back.
Rectangle / Horizonal only.
No rounded edges on the card.
White as the dominate color is preferred.

Target Market(s)

clients, legal, oil & gas, medical, professionals

Industry/Entity Type

IT, tech, consulting

Contact Information for Business Card

Name, Title, email, phone, cell, website

Font styles to use
Sans Serif

Requirements
Must have
• Clean design
Should not have
• loud colors or unusual fonts, etc

```html
<!DOCTYPE html>
<html lang="en">
<head>
<meta charset="utf-8">
<title>Nexora Solutions – Business Card</title>
<link rel="stylesheet" href="https://fonts.googleapis.com/css2?family=Montserrat:wght@800&family=Open+Sans:wght@400;700&display=swap">
<style>
  :root {
    --backdrop: #d6d6d6;
    --card-white: #ffffff;
    --card-dark: #141414;
    --navy: #241f66;
    --red: #ee3a4e;
    --yellow: #fdd22b;
    --sky: #41bbe9;
    --text-light: #ffffff;
  }
  * { box-sizing: border-box; margin: 0; padding: 0; }
  html, body {
    width: 1200px; height: 846px; overflow: hidden;
    background: var(--backdrop);
    font-family: "Open Sans", Arial, sans-serif;
  }
  .canvas { position: relative; width: 1200px; height: 846px; }

  .card {
    position: absolute;
    width: 530px; height: 303px;
    box-shadow: 0 18px 40px rgba(0,0,0,0.18);
    overflow: hidden;
  }

  /* Front */
  .card-front { left: 50px; top: 190px; background: var(--card-white); }
  .brand-block {
    position: absolute; left: 58px; top: 110px;
    display: flex; align-items: center; gap: 12px;
  }
  .brand-square { width: 34px; height: 34px; background: var(--navy); }
  .brand-name {
    font-family: "Open Sans", Arial, sans-serif; font-weight: 700;
    font-size: 34px; color: var(--navy); letter-spacing: -0.5px;
  }
  .contact-block { position: absolute; left: 290px; top: 62px; color: var(--navy); }
  .person-name {
    font-family: "Montserrat", Arial, sans-serif; font-weight: 800;
    font-size: 25px; line-height: 1; letter-spacing: -0.3px;
  }
  .person-title { font-size: 13px; margin-top: 4px; margin-bottom: 12px; }
  .contact-list { list-style: none; }
  .contact-item {
    display: flex; align-items: center; gap: 9px;
    font-size: 13.5px; line-height: 1.55;
  }
  .contact-icon { width: 13px; height: 13px; flex: none; fill: var(--navy); }
  .accent-strip { position: absolute; left: 0; right: 0; bottom: 0; height: 9px; display: flex; }
  .accent-strip span { flex: 1; }
  .strip-yellow { background: var(--yellow); }
  .strip-sky { background: var(--sky); }
  .strip-red { background: var(--red); }
  .strip-navy { background: var(--navy); }

  /* Back */
  .card-back { left: 620px; top: 343px; background: var(--card-dark); }
  .back-brand {
    position: absolute; inset: 0;
    display: flex; align-items: center; justify-content: center; gap: 10px;
  }
  .back-square { width: 22px; height: 22px; background: var(--red); }
  .back-name {
    font-family: "Open Sans", Arial, sans-serif; font-weight: 700;
    font-size: 24px; color: var(--text-light);
  }
</style>
</head>
<body>
<main class="canvas">

  <section class="card card-front" aria-label="Business card front">
    <div class="brand-block">
      <div class="brand-square"></div>
      <span class="brand-name">Nexora</span>
    </div>

    <div class="contact-block">
      <h1 class="person-name">Daniel Hart</h1>
      <p class="person-title">IT Consultant</p>
      <ul class="contact-list">
        <li class="contact-item">
          <svg class="contact-icon" viewBox="0 0 16 16"><path d="M1 3h14v10H1z M1 3l7 6 7-6" fill="var(--navy)" stroke="#fff" stroke-width="1.2"/></svg>
          daniel.hart@nexora.ca
        </li>
        <li class="contact-item">
          <svg class="contact-icon" viewBox="0 0 16 16"><path d="M3 1l3 3-1.5 2a9 9 0 0 0 5.5 5.5L12 10l3 3-2 2C7 15 1 9 1 3z"/></svg>
          (555) 014-2290
        </li>
        <li class="contact-item">
          <svg class="contact-icon" viewBox="0 0 16 16"><rect x="4" y="1" width="8" height="14" rx="1.5" fill="none" stroke="var(--navy)" stroke-width="1.4"/><circle cx="8" cy="12.5" r="0.9"/></svg>
          (555) 017-4418
        </li>
        <li class="contact-item">
          <svg class="contact-icon" viewBox="0 0 16 16"><g fill="none" stroke="var(--navy)" stroke-width="1.2"><circle cx="8" cy="8" r="6.5"/><ellipse cx="8" cy="8" rx="3" ry="6.5"/><path d="M1.5 8h13M2.5 4.5h11M2.5 11.5h11"/></g></svg>
          www.nexora.ca
        </li>
      </ul>
    </div>

    <div class="accent-strip">
      <span class="strip-yellow"></span>
      <span class="strip-sky"></span>
      <span class="strip-red"></span>
      <span class="strip-navy"></span>
    </div>
  </section>

  <section class="card card-back" aria-label="Business card back">
    <div class="back-brand">
      <div class="back-square"></div>
      <span class="back-name">Nexora Solutions</span>
    </div>
  </section>

</main>
</body>
</html>
```